Travel Website Design

My client is a startup that will sell luxury hunting and fishing trips.
We do not have a logo as of yet, but I have attached 3 options for you to use in the mockup process. Please feel free to use any one (or all 3) of them, but don't base design around them.

Also attached is client's loose idea of how he wants an interior page to look. For the homepage, it would definitely need a rotating image slider, a search, and a tabbed section. The crestpinesafaris.com is probably closest to what he is looking for.

Here are a few websites to pass along. In addition to the logos I have attached some links of company websites that are competition and have similar designs and layouts similar to what I am looking for.

http://www.crestpinesafaris.com - The most direct competition that I have. I really like how they layout the pages and lodges info.

Varno.com - Close competition. Not a huge fan of how they search for lodges but like how they display each lodge and provide info.

http://www.qrandel.com/ - Example of a company website and layout the client does not like.

http://stonemeadjourneys.com/ - Clean feel. Not a fan of how they layout each lodges info.

```html
<!DOCTYPE html>
<html lang="en">
<head>
<meta charset="utf-8">
<title>Ridgewater – Travel</title>
<link rel="stylesheet" href="https://fonts.googleapis.com/css2?family=Arimo:ital,wght@0,400;0,700;1,400&display=swap">
<style>
:root{
  --page:#f0f0f0;
  --panel:#ffffff;
  --band:#333333;
  --dark:#2b2b2b;
  --black:#0d0d0d;
  --text:#555555;
  --muted:#888888;
  --light:#aaaaaa;
  --accent:#f7870b;
  --line:#dddddd;
}
*{box-sizing:border-box;margin:0;padding:0}
html,body{width:1200px;height:1000px;overflow:hidden}
body{position:relative;background:var(--page);font-family:"Arimo",Arial,sans-serif;color:var(--text)}
.abs{position:absolute}
.backdrop{left:0;top:0;width:1200px;height:492px;
  background:linear-gradient(90deg,#1f3a4a 0%,#3e6a7a 14%,#7a8f7e 40%,#aeb79a 62%,#dcd9a0 82%,#eee7b2 100%)}
.backdrop::after{content:"";position:absolute;inset:0;background:linear-gradient(180deg,rgba(20,30,30,.35),rgba(0,0,0,0) 40%,rgba(10,20,25,.35))}
.helpline{left:234px;top:31px;font-size:10px;color:#fff;display:flex;align-items:center;gap:6px}
.helpline b{font-weight:700}
.social-top{left:876px;top:27px;width:87px;height:24px;background:var(--dark);display:flex;justify-content:space-around;align-items:center;padding:0 8px}
.social-top span{width:8px;height:8px;border-radius:50%;background:#fff}
.navbar{left:234px;top:63px;width:642px;height:83px;background:var(--panel)}
.brand{position:absolute;left:18px;top:31px;display:flex;align-items:center;gap:8px;font-size:14px;font-weight:700;color:#2a5d8f}
.brand i{width:18px;height:18px;background:#2a5d8f;display:block}
.menu{position:absolute;left:181px;top:32px;display:flex}
.menu a{text-decoration:none;display:block;margin-right:0}
.menu small{display:block;font-size:8px;font-style:italic;color:var(--light);line-height:10px}
.menu strong{display:block;font-size:10px;font-weight:400;color:#444;line-height:14px;margin-top:1px}
.search-box{left:876px;top:63px;width:87px;height:83px;background:#333;display:flex;align-items:center;justify-content:center}
.hero{left:234px;top:146px;width:729px;height:346px;background:linear-gradient(180deg,#8fa887 0%,#6f8b66 35%,#5d6b4d 60%,#8e8a73 100%)}
.slider-dots{left:557px;top:457px;width:80px;height:27px;background:#fff;display:flex;justify-content:center;align-items:center;gap:4px}
.slider-dots span{width:7px;height:7px;border-radius:50%;background:#777}
.slider-dots span.on{background:var(--accent)}
.finder{left:0;top:492px;width:1200px;height:53px;background:var(--band)}
.finder-label{left:234px;top:512px;font-size:12.5px;color:#e0e0e0}
.finder-select{left:425px;top:504px;width:142px;height:31px;border:1px solid #666;background:#444;border-radius:3px;color:#ddd;font-size:9.5px;padding:9px 11px}
.finder-select::after{content:"";position:absolute;right:11px;top:13px;border:5px solid transparent;border-top:6px solid #bbb}
.book-btn{left:772px;top:504px;width:190px;height:31px;background:var(--black);color:#999;font-size:10.5px;font-style:italic;text-align:center;line-height:31px;letter-spacing:.3px}
.welcome-title{left:235px;top:576px;font-size:17px;font-weight:700;color:#555}
.welcome-text{left:234px;top:610px;width:520px;font-size:8px;line-height:12.4px;color:#666}
.newsletter{left:774px;top:578px;width:189px;height:120px;background:#fff;border:1px solid var(--line)}
.newsletter h3{position:absolute;left:20px;top:15px;font-size:8.5px;font-weight:400;color:#444;letter-spacing:.2px}
.newsletter hr{position:absolute;left:20px;top:31px;width:147px;border:0;border-top:1px solid var(--line)}
.email-field{position:absolute;left:21px;top:38px;width:147px;height:29px;border:1px solid var(--line);font-size:6.5px;color:#aaa;padding:10px 8px}
.subscribe-btn{position:absolute;left:21px;top:70px;width:147px;height:26px;background:var(--accent);color:#fff;font-size:9.5px;text-align:center;line-height:26px}
.shadow-curve{left:234px;top:712px;width:729px;height:14px}
.tabs-panel{left:234px;top:720px;width:729px;height:230px;background:var(--panel)}
.tab{position:absolute;left:26px;font-size:11px;color:#777}
.tab.active{color:var(--accent)}
.tab-line{position:absolute;left:26px;top:57px;width:129px;border-top:1px solid var(--line)}
.card{position:absolute;top:37px;width:145px}
.card .photo{width:145px;height:90px}
.card p{font-size:8px;line-height:12.5px;color:#666;margin-top:7px}
.card a{display:block;font-size:6.5px;color:var(--accent);text-decoration:none;margin-top:7px}
.trip-list{position:absolute;left:526px;top:38px;list-style:none}
.trip-list li{font-size:7.8px;color:#555;height:21px;display:flex;gap:8px}
.trip-list li svg{margin-top:1px}
.trip-list li.new span{color:var(--accent);text-decoration:underline}
.footer-text{left:234px;top:974px;font-size:7.8px;color:#666}
.footer-text b{color:#444}
.social-foot{left:896px;top:970px;display:flex;gap:3px}
.social-foot span{width:14px;height:14px;border-radius:2px;background:#8a8a8a}
</style>
</head>
<body>
<div class="abs backdrop" role="img" aria-label="Blurred lakeside landscape backdrop"></div>

<div class="abs helpline">
  <svg width="10" height="10" viewBox="0 0 24 24"><path fill="#fff" d="M6.6 10.8a15 15 0 0 0 6.6 6.6l2.2-2.2c.3-.3.7-.4 1-.2 1.1.4 2.3.6 3.6.6.6 0 1 .4 1 1V20c0 .6-.4 1-1 1A17 17 0 0 1 3 4c0-.6.4-1 1-1h3.5c.6 0 1 .4 1 1 0 1.3.2 2.5.6 3.6.1.3 0 .7-.2 1z"/></svg>
  Need some help? Call us: <b>+123 4470 21986</b>
</div>
<div class="abs social-top"><span></span><span></span><span></span><span></span></div>

<header class="abs navbar">
  <div class="brand"><i></i>Ridgewater</div>
  <nav class="menu">
    <a href="#" style="width:65px"><small>Welcome</small><strong>HOME</strong></a>
    <a href="#" style="width:102px"><small>Who we are</small><strong>CONSERVATION</strong></a>
    <a href="#" style="width:68px"><small>What Says</small><strong>BLOGS</strong></a>
    <a href="#" style="width:85px"><small>Need to us</small><strong>TRAVEL TOOL</strong></a>
    <a href="#" style="width:62px"><small>Becomes a</small><strong>MEMBER</strong></a>
    <a href="#"><small>Get in Touch</small><strong>CONTACT US</strong></a>
  </nav>
</header>
<div class="abs search-box">
  <svg width="20" height="20" viewBox="0 0 20 20"><circle cx="7" cy="7" r="5" fill="none" stroke="#ccc" stroke-width="2"/><line x1="11" y1="11" x2="18" y2="17" stroke="#ccc" stroke-width="3" stroke-linecap="round"/></svg>
</div>

<div class="abs hero" role="img" aria-label="Slider photo: two young anglers fishing from a tree trunk over a calm lake"></div>
<div class="abs slider-dots"><span></span><span></span><span class="on"></span><span></span><span></span></div>

<div class="abs finder"></div>
<div class="abs finder-label">Select Your Destination for Travel</div>
<div class="abs finder-select">Select Destination</div>
<div class="abs book-btn">BOOK YOUR TRIP NOW !</div>

<h1 class="abs welcome-title">WELCOME TO OUR WEBSITE !</h1>
<p class="abs welcome-text">Lorem Ipsum is simply dummy text of the printing and typesetting industry. Lorem Ipsum has been the industry's standard dummy text ever since the 1500s, when an unknown printer took a galley of type and scrambled it to make a type specimen book. It has survived not only five centuries, but also the leap into electronic typesetting, remaining essentially unchanged. It was popularised in the 1960s with the release of Pressline sheets containing Lorem Ipsum passages, and more recently with desktop publishing software like Quillset Layout including versions of Lorem Ipsum.</p>

<aside class="abs newsletter">
  <h3>SUBSCRIBE NEWSLETTER</h3>
  <hr>
  <div class="email-field">YOUR EMAIL</div>
  <div class="subscribe-btn">SUBSCRIBE NOW !</div>
</aside>

<svg class="abs shadow-curve" viewBox="0 0 729 14" preserveAspectRatio="none">
  <defs><radialGradient id="shade" cx="50%" cy="0%" r="60%"><stop offset="0" stop-color="#000" stop-opacity=".45"/><stop offset="1" stop-color="#000" stop-opacity="0"/></radialGradient></defs>
  <path d="M0 8 Q364 -2 729 8 L729 14 L0 14Z" fill="url(#shade)"/>
</svg>

<section class="abs tabs-panel">
  <div class="tab active" style="top:36px">Featured Trip</div>
  <div class="tab-line"></div>
  <div class="tab" style="top:72px">Travel Blogs</div>
  <div class="tab" style="top:107px">Trips Trending Now</div>
  <div class="tab" style="top:141px">Featured Destinations</div>

  <div class="card" style="left:199px">
    <div class="photo" role="img" aria-label="Angler silhouetted on a lake shore at sunset" style="background:linear-gradient(180deg,#9fb4c8 0%,#e8c27a 45%,#3a3a32 60%,#6f7e88 100%)"></div>
    <p>Lorem Ipsum is simply dummy text of the printing and typesetting industry.</p>
    <a href="#">READ MORE</a>
  </div>
  <div class="card" style="left:362px">
    <div class="photo" role="img" aria-label="Angler holding a large orange fish beside a lake" style="background:linear-gradient(135deg,#5d7a6a 0%,#7c8d7a 35%,#ee7a2a 55%,#d8621c 75%,#51636a 100%)"></div>
    <p>Lorem Ipsum is simply dummy text of the printing and typesetting industry.</p>
    <a href="#" style="margin-left:2px">READ MORE</a>
  </div>

  <ul class="trip-list">
    <li><svg width="7" height="7" viewBox="0 0 10 10"><path d="M1 5l3 3 5-6" fill="none" stroke="#444" stroke-width="1.6"/></svg><span>Rajasthan's Pushkar Festival</span></li>
    <li><svg width="7" height="7" viewBox="0 0 10 10"><path d="M1 5l3 3 5-6" fill="none" stroke="#444" stroke-width="1.6"/></svg><span>Walking Japan: Village to Village</span></li>
    <li><svg width="7" height="7" viewBox="0 0 10 10"><path d="M1 5l3 3 5-6" fill="none" stroke="#444" stroke-width="1.6"/></svg><span>Cultural Tour and Trek in the Himalayas</span></li>
    <li><svg width="7" height="7" viewBox="0 0 10 10"><path d="M1 5l3 3 5-6" fill="none" stroke="#444" stroke-width="1.6"/></svg><span>Pura Vida in Costa Rica!</span></li>
    <li class="new"><svg width="7" height="7" viewBox="0 0 10 10"><path d="M1 5l3 3 5-6" fill="none" stroke="#f7870b" stroke-width="1.6"/></svg><span>NEW! Mongolia: Horses, Camels and Nomads</span></li>
    <li><svg width="7" height="7" viewBox="0 0 10 10"><path d="M1 5l3 3 5-6" fill="none" stroke="#444" stroke-width="1.6"/></svg><span>Galápagos Wildlife Adventure Cruise</span></li>
  </ul>
</section>

<footer>
  <div class="abs footer-text">Call: <b>+1 4470 2198 600</b> &nbsp;&nbsp;|&nbsp;&nbsp; Copyright © 2014 Ridgewater.</div>
  <div class="abs social-foot"><span></span><span></span><span></span><span></span></div>
</footer>
</body>
</html>
```